Geothermal company needs a creative "POW" business card

Manufacturers tend to be boring. We are not! We are a Geothermal Heat Pump company that has over 30 yrs of experience and wants a new look and updated feel. Nothing old (yawn) so get your creative hats on and let's rock!

We want to use the great colors of lime green and navy blue. Our new logo is attached and we're ready to roll. Remember, we're a professional leader in the geothermal industry that needs to make an eye catching and memorable first glance.

```html
<!DOCTYPE html>
<html lang="en">
<head>
<meta charset="utf-8">
<title>Borealis Thermal – Business Card</title>
<link rel="stylesheet" href="https://fonts.googleapis.com/css2?family=Source+Sans+3:wght@400;600&family=Tinos:wght@400;700&display=swap">
<style>
  :root {
    --backdrop: #3b3733;
    --card: #dcdcde;
    --band: #f1f1f2;
    --lime: #7cbf3a;
    --navy: #1d3a6e;
    --ink: #2a2a2a;
    --muted: #555;
  }
  * { box-sizing: border-box; margin: 0; padding: 0; }
  html, body { width: 1117px; height: 1200px; overflow: hidden; }
  body { background: var(--backdrop); position: relative; font-family: "Tinos", "Times New Roman", serif; color: var(--ink); }

  .card { position: absolute; left: 98px; width: 904px; height: 514px; background: var(--card); border-radius: 34px; box-shadow: 0 4px 18px rgba(0,0,0,.35); }
  .card--front { top: 65px; }
  .card--back { top: 625px; }

  .brand { position: absolute; left: 132px; top: 42px; display: flex; align-items: center; gap: 30px; }
  .brand__mark { width: 130px; height: 130px; border-radius: 50%; background: var(--navy); flex: none; }
  .brand__name { font-family: "Source Sans 3", sans-serif; font-weight: 600; font-size: 74px; line-height: 1; color: var(--lime); }
  .brand__tagline { font-family: "Source Sans 3", sans-serif; font-weight: 600; font-size: 20px; color: var(--navy); margin-top: 8px; }

  .holder { position: absolute; top: 240px; left: 0; width: 100%; text-align: center; font-size: 29px; color: var(--navy); }
  .holder strong { font-weight: 700; }

  .phones { position: absolute; left: 172px; top: 290px; width: 529px; height: 63px; background: var(--band); box-shadow: 0 10px 10px -6px rgba(0,0,0,.25); display: flex; align-items: center; justify-content: center; gap: 28px; font-size: 22px; }
  .online { position: absolute; left: 17px; top: 384px; width: 852px; height: 60px; background: var(--band); display: flex; align-items: center; justify-content: center; gap: 30px; font-size: 22px; }
  .address { position: absolute; top: 462px; left: 0; width: 100%; display: flex; justify-content: center; align-items: center; gap: 10px; font-size: 22px; }

  .contact { display: inline-flex; align-items: center; gap: 8px; }
  .icon { width: 20px; height: 20px; fill: var(--ink); flex: none; }

  .back-brand { position: absolute; left: 0; top: 70px; width: 100%; display: flex; flex-direction: column; align-items: center; gap: 26px; }
  .back-brand__mark { width: 260px; height: 260px; border-radius: 50%; background: var(--navy); }
  .back-brand__name { font-family: "Source Sans 3", sans-serif; font-weight: 600; font-size: 46px; color: var(--lime); line-height: 1; }
  .back-url { position: absolute; left: 0; top: 440px; width: 100%; text-align: center; font-size: 29px; letter-spacing: 3px; color: var(--ink); }
</style>
</head>
<body>
  <section class="card card--front">
    <div class="brand">
      <div class="brand__mark"></div>
      <div>
        <div class="brand__name">Borealis Thermal</div>
        <div class="brand__tagline">Manufacturer of Geothermal Heat Pumps for the North</div>
      </div>
    </div>

    <p class="holder"><strong>Kent Marlow,</strong> CEO</p>

    <div class="phones">
      <span class="contact">
        <svg class="icon" viewBox="0 0 24 24"><path d="M6.6 10.8a15 15 0 0 0 6.6 6.6l2.2-2.2c.3-.3.7-.4 1-.2 1.1.4 2.3.6 3.6.6.6 0 1 .4 1 1V20c0 .6-.4 1-1 1A17 17 0 0 1 3 4c0-.6.4-1 1-1h3.5c.6 0 1 .4 1 1 0 1.3.2 2.5.6 3.6.1.3 0 .7-.2 1z"/></svg>
        (555) 014-2200
      </span>
      <span class="contact">
        <svg class="icon" viewBox="0 0 24 24"><path d="M5 11l2-5h10l2 5h1v7h-2v2h-3v-2H9v2H6v-2H4v-7zm2.4 0h9.2l-1.2-3H8.6zM7 13.5a1.3 1.3 0 1 0 0 2.6 1.3 1.3 0 0 0 0-2.6zm10 0a1.3 1.3 0 1 0 0 2.6 1.3 1.3 0 0 0 0-2.6z"/></svg>
        (555) 014-2201
      </span>
    </div>

    <div class="online">
      <span class="contact">
        <svg class="icon" viewBox="0 0 24 24"><path d="M3 6h18v12H3zm2 2v.5l7 4.5 7-4.5V8l-7 4.5z"/></svg>
        kentmarlow@borealisthermal.com
      </span>
      <span class="contact">
        <svg class="icon" viewBox="0 0 24 24"><path d="M12 2a10 10 0 1 0 0 20 10 10 0 0 0 0-20zm6.9 9h-3a15 15 0 0 0-1.3-5.6A8 8 0 0 1 18.9 11zM12 4c.9 1.2 1.8 3.6 1.9 7h-3.8c.1-3.4 1-5.8 1.9-7zM9.4 5.4A15 15 0 0 0 8.1 11h-3a8 8 0 0 1 4.3-5.6zM5.1 13h3a15 15 0 0 0 1.3 5.6A8 8 0 0 1 5.1 13zM12 20c-.9-1.2-1.8-3.6-1.9-7h3.8c-.1 3.4-1 5.8-1.9 7zm2.6-1.4a15 15 0 0 0 1.3-5.6h3a8 8 0 0 1-4.3 5.6z"/></svg>
        www.borealisthermal.com
      </span>
    </div>

    <div class="address">
      <svg class="icon" viewBox="0 0 24 24"><path d="M12 3l10 9h-3v9h-5v-6h-4v6H5v-9H2z"/></svg>
      42 Birch Lake Rd, Elmford, MN 56000
    </div>
  </section>

  <section class="card card--back">
    <div class="back-brand">
      <div class="back-brand__mark"></div>
      <div class="back-brand__name">Borealis Thermal</div>
    </div>
    <p class="back-url">www.borealisthermal.com</p>
  </section>
</body>
</html>
```